Hardcore nerd needs to stand out in a sea of dull Defence business cards

Wombat Devices is a new Australian consulting engineering company that turns research and theory into practical systems. No evangelistic fluff, just mathematics and physics into electronic and optical circuits for consumer products, scientific research or Defence applications.

We already have a recognised logo (provided) which is often dark blue/black on a light background but we're open to other combinations. (Us engineers tend to have limited aesthetic imagination :)

Some of our recent products have included:
* Instrumentation for electrical testing,
* Radar jammers,
* GPS antenna design,
* Satellite tracking systems,
* High power lasers

We're open to both single and double-sided designs - happy to be convinced either way.

P.S. Another group is working on the web page, so - alas - our web site is currently of no use for images/ideas...

Target Market(s)

Engineering managers,
Scientists

Contact Information for Business Card

Dr Colin Marsh
R&D Engineer

colin@wombatdevicesco.com.au
0427 563 210

PO Box XXX (to be confirmed)
Banks ACT 2913
Australia

Font styles to use
Serif
Sans Serif

Colors

Designer to choose colors to be used in the design.

Requirements
Must have
• My contact details!
• I've had many (great) "bold and plain" designs submitted already, so feel free to be artistically creative :)
• Happy to take advice re fonts/colours/printability etc.
Nice to have
• I'm not sure if "lists" are more at home on a CV than a business card, but representative services include:
• Applied electromagnetics
• RF and high speed electronics
• Signal and image processing
• Electro-optical and laser systems
• Concept-to-prototype design services
• If you're considering double sided cards, then often measuring/alignment grids/rulers feature on the back of similar cards.
• e.g. https://www.lumoptix-example.com/newgrouppage9.cfm?objectgroup_id=4815
• https://www.lumoptix-example.com/newgrouppage9.cfm?objectgroup_ID=4817
• ..or even a "Smith chart" (google will return lots)
• Generic images to represent a capability might work - googling images associated with keyword for each of these areas might help:
• - "passive radar", "phased array", "fdtd", "vircator"
• RF and high speed electronic design
• - "smith chart", "microstrip circuits", "dimensioned drawing", "electronic schematic"
• - "dft", "iir filter"
• - "optical cavity". "laser energy level diagram"
• Background/watermarked images outlines/wireframes/schematics would probably look OK.
Should not have
• If a list of projects/services is provided, it is important not to make the client feel that this is "all" the company can do. Engineering design is a creative discipline (like graphics :)
• Please, no stock "military" snaps like planes, missiles, etc!

```html
<!DOCTYPE html>
<html lang="en">
<head>
<meta charset="utf-8">
<title>Wombat Devices – Business Card</title>
<link rel="stylesheet" href="https://fonts.googleapis.com/css2?family=Lato:wght@400;700;900&display=swap">
<style>
  :root {
    --navy: #2a2f78;
    --navy-soft: #3a408c;
    --orange: #f07d1a;
    --white: #ffffff;
    --backdrop: #e9e8e4;
    --pattern-light: #d9dbec;
  }
  * { box-sizing: border-box; margin: 0; padding: 0; }
  html, body { width: 1200px; height: 835px; overflow: hidden; }
  body {
    background: var(--backdrop);
    font-family: "Lato", Arial, sans-serif;
    display: flex;
    flex-direction: column;
    align-items: center;
    justify-content: center;
    gap: 40px;
  }
  .card {
    position: relative;
    width: 620px;
    height: 354px;
    border-radius: 22px;
    overflow: hidden;
    box-shadow: 0 4px 14px rgba(0,0,0,0.15);
  }

  /* Front */
  .card-front { background: var(--white); }
  .edge-band {
    position: absolute;
    top: 0; bottom: 0;
    width: 40px;
    background: linear-gradient(90deg, var(--navy) 0 45%, var(--pattern-light) 45% 100%);
  }
  .edge-band.left { left: 0; }
  .edge-band.right { right: 0; transform: scaleX(-1); }

  .brand {
    position: absolute;
    top: 58px;
    left: 0; right: 0;
    display: flex;
    align-items: center;
    justify-content: center;
    gap: 14px;
  }
  .brand-dot {
    width: 46px; height: 46px;
    border-radius: 50%;
    background: var(--navy);
  }
  .brand-name {
    font-weight: 900;
    font-size: 30px;
    letter-spacing: 1px;
    text-transform: uppercase;
    color: var(--navy);
  }

  .person {
    position: absolute;
    left: 78px;
    top: 186px;
  }
  .person-name {
    font-weight: 700;
    font-size: 24px;
    color: var(--orange);
  }
  .person-role {
    font-weight: 700;
    font-size: 17px;
    color: var(--navy);
    margin-top: 2px;
  }

  .contact {
    position: absolute;
    right: 74px;
    top: 174px;
    text-align: center;
    color: var(--navy);
  }
  .contact-icons {
    display: flex;
    justify-content: center;
    gap: 8px;
    padding-bottom: 4px;
    border-bottom: 1px solid var(--navy);
    width: 140px;
    margin: 0 auto 6px;
  }
  .contact-icons svg { width: 14px; height: 14px; }
  .contact-phone { font-size: 17px; }
  .contact-email { font-size: 15px; margin-top: 2px; }

  .address {
    position: absolute;
    left: 0; right: 0;
    bottom: 44px;
    text-align: center;
    font-weight: 700;
    font-size: 17px;
    color: var(--navy);
  }

  /* Back */
  .card-back { background: var(--navy); }
  .pattern-strip {
    position: absolute;
    left: 0; right: 0;
    height: 38px;
    background: linear-gradient(180deg, var(--pattern-light) 0 50%, var(--navy-soft) 50% 100%);
  }
  .pattern-strip.top { top: 0; }
  .pattern-strip.bottom { bottom: 0; transform: scaleY(-1); }

  .back-brand {
    position: absolute;
    top: 70px;
    left: 0; right: 0;
    display: flex;
    flex-direction: column;
    align-items: center;
    gap: 10px;
  }
  .back-brand .brand-dot {
    width: 60px; height: 60px;
    background: var(--orange);
  }
  .back-brand .brand-name {
    color: var(--white);
    font-size: 24px;
  }
  .services {
    position: absolute;
    top: 190px;
    left: 0; right: 0;
    list-style: none;
    text-align: center;
    color: var(--white);
    font-size: 18px;
    line-height: 1.22;
  }
</style>
</head>
<body>

  <section class="card card-front">
    <div class="edge-band left" role="img" aria-label="Repeating band of the company mark along the left edge"></div>
    <div class="edge-band right" role="img" aria-label="Repeating band of the company mark along the right edge"></div>

    <div class="brand">
      <span class="brand-dot"></span>
      <span class="brand-name">Wombat Devices</span>
    </div>

    <div class="person">
      <p class="person-name">Dr Colin Marsh</p>
      <p class="person-role">R&amp;D Engineer</p>
    </div>

    <div class="contact">
      <div class="contact-icons">
        <svg viewBox="0 0 24 24" aria-hidden="true"><path fill="#f07d1a" d="M6.6 10.8a15 15 0 0 0 6.6 6.6l2.2-2.2a1 1 0 0 1 1-.25 11.4 11.4 0 0 0 3.6.57 1 1 0 0 1 1 1V20a1 1 0 0 1-1 1A17 17 0 0 1 3 4a1 1 0 0 1 1-1h3.5a1 1 0 0 1 1 1c0 1.25.2 2.45.57 3.57a1 1 0 0 1-.25 1z"/></svg>
        <svg viewBox="0 0 24 24" aria-hidden="true"><rect x="3" y="6" width="18" height="13" rx="1.5" fill="none" stroke="#f07d1a" stroke-width="2"/><path d="M3.5 7l8.5 6.5L20.5 7" fill="none" stroke="#f07d1a" stroke-width="2"/></svg>
      </div>
      <p class="contact-phone">0427 563 210</p>
      <p class="contact-email">colin@wombatdevicesco.com.au</p>
    </div>

    <p class="address">PO Box XXX, Banks ACT 2913, Australia</p>
  </section>

  <section class="card card-back">
    <div class="pattern-strip top" role="img" aria-label="Repeating band of the company mark along the top edge"></div>
    <div class="pattern-strip bottom" role="img" aria-label="Repeating band of the company mark along the bottom edge"></div>

    <div class="back-brand">
      <span class="brand-dot"></span>
      <span class="brand-name">Wombat Devices</span>
    </div>

    <ul class="services">
      <li>Radar jammers,</li>
      <li>High power lasers,</li>
      <li>GPS antenna design,</li>
      <li>Satellite tracking systems,</li>
      <li>Instrumentation for electrical testing</li>
    </ul>
  </section>

</body>
</html>
```